Welding and farication business card

Business name Tbm Welding & Fabrication

I need a business card made for my welding and fabrication business that is bold and stands out. My business is both welding repairs on machinery and anything else you can imagine as well as fabricating new products. i have used this service before and was very happy with the out come of my design logo. i think the card should remain fairly simple and classy but also be bold. I think a black card would best be suited to the talk with my logo on it. i feel the back of the card should just have my logo and the front have my logo email, website and phone number and maybe incorporate a facebook and instagram simple if it can be made look good these arnt a necessity.
I have included both my logo and some business card ideas below

Target Market(s)

Farmers, heavy industry, earthmoving, trucking

Industry/Entity Type

Engineering

Contact Information for Business Card

0438517264
dale@tbmweldingandfabrication.com.au
www.tbmweldingandfabrication.com.au

Colors
33a6d7
0255a3

Requirements
Must have
• Dale Hutchins
my phone number 0438517264
my logo
Preferably a black card desgn
Nice to have
• List of what i do,
Sheds and carports
Ute trays
Stockyards
Trailers
Farm equipment
Stockcrates
Gateways and Entrances
Breakdowns
Maintenance
And lots more!

```html
<!DOCTYPE html>
<html lang="en">
<head>
<meta charset="utf-8">
<title>Tbm Welding &amp; Fabrication – Business Card</title>
<link href="https://fonts.googleapis.com/css2?family=Josefin+Sans:wght@300;400;600&display=swap" rel="stylesheet">
<style>
  :root {
    --stage: #2a2a2c;
    --card-black: #1c1c1e;
    --card-white: #f1f2f3;
    --brand-blue: #0255a3;
    --band-blue: #2f6db0;
    --sky-blue: #33a6d7;
    --steel-grey: #5d6673;
    --text-light: #d9dbde;
    --text-muted: #b8bcc2;
  }
  * { box-sizing: border-box; margin: 0; padding: 0; }
  html, body {
    width: 1200px; height: 900px; overflow: hidden;
    background: var(--stage);
    font-family: "Josefin Sans", sans-serif;
  }
  .canvas {
    width: 1200px; height: 900px;
    display: flex; flex-direction: column; align-items: center; justify-content: center;
    gap: 36px;
  }
  .card {
    position: relative;
    width: 700px; height: 400px;
    border-radius: 30px;
    overflow: hidden;
    background: var(--card-black);
    box-shadow: 0 10px 30px rgba(0,0,0,.45);
  }
  .card-bands { position: absolute; inset: 0; width: 100%; height: 100%; }

  /* Brand name block */
  .brand {
    position: absolute;
    display: flex; align-items: center; gap: 14px;
  }
  .brand-dot {
    width: 22px; height: 22px; border-radius: 50%;
    background: var(--sky-blue);
    flex: none;
  }
  .brand-name {
    font-weight: 600;
    color: var(--brand-blue);
    text-transform: uppercase;
    line-height: 1.05;
    letter-spacing: 1px;
  }

  /* Front */
  .front .brand { left: 150px; top: 58px; }
  .front .brand-name { font-size: 34px; }
  .holder-name {
    position: absolute; left: 38px; top: 300px;
    font-size: 26px; font-weight: 400; letter-spacing: 2px;
    color: var(--brand-blue); text-transform: uppercase;
  }
  .contact-list {
    position: absolute; right: 34px; bottom: 30px;
    list-style: none;
    display: flex; flex-direction: column; align-items: flex-end; gap: 6px;
  }
  .contact-item {
    display: flex; align-items: center; gap: 10px;
    font-size: 16px; font-weight: 300; color: var(--text-light);
  }
  .contact-item.phone { font-size: 20px; }
  .contact-icon {
    width: 20px; height: 20px; border-radius: 50%;
    background: var(--band-blue);
    display: flex; align-items: center; justify-content: center;
    flex: none;
  }
  .contact-icon svg { width: 12px; height: 12px; }

  /* Back */
  .back .brand { left: 46px; top: 150px; }
  .back .brand-name { font-size: 30px; color: var(--band-blue); }
  .services {
    position: absolute; right: 46px; top: 70px;
    list-style: none;
    display: flex; flex-direction: column; gap: 6px;
  }
  .service {
    font-size: 19px; font-weight: 300; color: var(--text-muted);
    display: flex; align-items: center; gap: 10px;
  }
  .service::before {
    content: ""; width: 5px; height: 5px; border-radius: 50%;
    background: var(--band-blue);
  }
</style>
</head>
<body>
<main class="canvas">

  <section class="card front" aria-label="Card front">
    <svg class="card-bands" viewBox="0 0 700 400" preserveAspectRatio="none" aria-hidden="true">
      <path d="M0,0 H700 V225 C520,262 260,240 0,130 Z" fill="var(--card-white)"/>
      <path d="M0,130 C260,240 520,262 700,225 V252 C520,278 260,250 0,134 Z" fill="var(--sky-blue)"/>
      <path d="M0,137 C260,254 520,282 700,258 V265 C520,291 260,280 0,185 Z" fill="var(--steel-grey)"/>
      <path d="M0,188 C260,284 520,296 700,270 V298 C520,320 260,298 0,196 Z" fill="var(--band-blue)"/>
    </svg>

    <div class="brand">
      <span class="brand-dot"></span>
      <span class="brand-name">Tbm Welding<br>&amp; Fabrication</span>
    </div>

    <p class="holder-name">Dale Hutchins</p>

    <ul class="contact-list">
      <li class="contact-item phone">0438517264
        <span class="contact-icon">
          <svg viewBox="0 0 12 12"><path d="M3 1 L5 3 L4 4.5 C4.6 6 6 7.4 7.5 8 L9 7 L11 9 L9.5 11 C5 10.5 1.5 7 1 2.5 Z" fill="#fff"/></svg>
        </span>
      </li>
      <li class="contact-item">dale@tbmweldingandfabrication.com.au
        <span class="contact-icon">
          <svg viewBox="0 0 12 12"><rect x="1" y="3" width="10" height="6.5" fill="none" stroke="#fff" stroke-width="1.1"/><path d="M1 3 L6 7 L11 3" fill="none" stroke="#fff" stroke-width="1.1"/></svg>
        </span>
      </li>
      <li class="contact-item">www.tbmweldingandfabrication.com.au
        <span class="contact-icon"></span>
      </li>
    </ul>
  </section>

  <section class="card back" aria-label="Card back">
    <div class="brand">
      <span class="brand-dot"></span>
      <span class="brand-name">Tbm Welding<br>&amp; Fabrication</span>
    </div>

    <ul class="services">
      <li class="service">Sheds and carports</li>
      <li class="service">Ute trays</li>
      <li class="service">Stockyards</li>
      <li class="service">Trailers</li>
      <li class="service">Farm equipment</li>
      <li class="service">Stockcrates</li>
      <li class="service">Gateways and Entrances</li>
      <li class="service">Breakdowns</li>
      <li class="service">Maintenance, And lots more!</li>
    </ul>
  </section>

</main>
</body>
</html>
```